Modern and Clean Web Re-Design Project

We have 2 companies in similar industries: Printing and Mail Preparation/Fulfillment. We prefer sites that are clean and easy to navigate.Our printing company, Harbourline Press Works' website, hpwgroup-example.ca is outdated needs revamping. We have rebranded our logo and are looking for a new design that is clean, modern and geared to other corporations and business in the downtown Toronto area. Our mailing company, The Parcel Loft (theparcelloft-example.ca) needs a website as well. This company is in the Direct Mail and letter shop business, which essentially is addressing/personalizing people's printed matter and preparing it for either the Canadian or US postal service. The Parcel Loft specializes in not-for-profit and corporate sectors.Please see our logos to get an idea of the colors and look we want. For all intensive purposes, the sites can look similar in design all we want is that each site has the appropriate corporate colors and is a bit different so they don't look identical as the two business run as separate corporations.The content of the website should be easily changed by our staff and we want it to be setup to optimized for SEO based on the keywords we want. We are looking for someone to work on this project immediately

After doing some thinking, I would like the site to be more modern but the non flash sites that I have seen so far Im finding life-less and while I want something clean, not overly busy and corporate looking, I dont want the design to be bland looking.

Please design with the previous specs in mind but with a twist as mentioned above.

Thanks
Dorian

Target Market(s)

See above

Industry/Entity Type

Printing

Requirements
Must have
• Must match the design and style of each respective logoSee the attached impage of the front of our offices to have an idea of our lookWe must be able to edit the content ourselves without any fancy programs or tools.Must be SEO optimized
Nice to have
• An online order form that can be emailed to us for quotes.....perhaps a page with a bunch of fields that have drop down menus....
Should not have
• Should not be overly busy. I want it to be clean and simple but informative without being hard to navigate

```html
<!DOCTYPE html>
<html lang="en">
<head>
<meta charset="utf-8">
<title>Harbourline Press Works</title>
<link href="https://fonts.googleapis.com/css2?family=Arimo:wght@400;700&display=swap" rel="stylesheet">
<style>
:root{
  --red:#f04e30;
  --orange:#fbb034;
  --orange-deep:#f5a623;
  --dark:#333333;
  --text:#555555;
  --muted:#8a8a8a;
  --line:#e6e6e6;
  --white:#ffffff;
}
*{box-sizing:border-box;margin:0;padding:0}
html,body{width:998px;height:1200px;overflow:hidden;background:var(--white)}
body{font-family:"Arimo",Arial,sans-serif;color:var(--text);position:relative}
.abs{position:absolute}

.brand{left:100px;top:38px;font-size:18px;font-weight:700;color:var(--red);display:flex;align-items:center;gap:8px}
.brand-mark{width:14px;height:14px;background:var(--orange);border-radius:50%}
.phone{right:100px;top:18px;display:flex;align-items:center;gap:7px;font-size:16px;color:var(--dark)}
.phone-icon{width:20px;height:20px;background:#8c8c8c;border-radius:3px;display:flex;align-items:center;justify-content:center}
.main-nav{right:100px;top:62px;display:flex;gap:0;font-size:12.5px}
.main-nav a{color:var(--red);text-decoration:none;padding:5px 0 5px 36px;line-height:14px}
.main-nav a.active{background:var(--red);color:var(--white);padding:5px 11px;border-radius:1px;margin-right:-8px}

.slider{left:100px;top:126px;width:798px;height:322px;background:#efefef;padding:4px}
.slider-shadow{left:130px;top:446px;width:738px;height:18px;border-radius:50%;background:radial-gradient(ellipse at center top,rgba(0,0,0,.55),rgba(0,0,0,0) 70%)}
.slide{position:relative;width:100%;height:100%;overflow:hidden;
  background:linear-gradient(90deg,#e9e4de 0%,#f1efec 30%,#d8dcde 55%,#c9ced2 75%,#b9bfc4 100%)}
.slide-photo{position:absolute;inset:0}
.slide-title{position:absolute;left:420px;top:60px;font-size:39px;font-weight:700;color:var(--orange);letter-spacing:.5px;text-shadow:0 1px 0 rgba(0,0,0,.15)}
.slide-tag{position:absolute;left:421px;top:106px;background:var(--red);color:var(--white);font-weight:700;font-size:14.5px;padding:3px 7px;letter-spacing:.4px}
.slide-points{position:absolute;left:421px;top:164px;list-style:none}
.slide-points li{display:flex;align-items:center;gap:14px;height:42px;font-size:15px;color:#222}
.tick{width:26px;height:26px;border-radius:50%;background:var(--orange);display:flex;align-items:center;justify-content:center}
.arrow{position:absolute;top:141px;width:34px;height:34px;border-radius:50%;background:#2e2e2e;display:flex;align-items:center;justify-content:center}
.arrow.prev{left:12px}.arrow.next{right:12px}

.services{left:100px;top:500px;width:798px;display:flex}
.service{width:206px;text-align:center;margin-right:-2px}
.service svg{height:60px}
.service h3{font-weight:400;font-size:17.5px;color:#222;margin-top:10px}
.service p{font-size:10.5px;line-height:13.5px;color:var(--muted);margin-top:6px;padding:0 4px;letter-spacing:.3px}

.divider{height:1px;background:linear-gradient(90deg,rgba(230,230,230,0),var(--line) 15%,var(--line) 85%,rgba(230,230,230,0))}

.about{left:100px;top:696px;width:503px}
.about h2{font-size:15px;font-weight:700;color:#222;margin-bottom:12px}
.about-photo{float:left;width:172px;height:86px;border:3px solid #f0f0f0;margin:0 11px 6px 0;background:linear-gradient(90deg,#d9dde2,#c4ccd6 45%,#e9e1d8)}
.about p{font-size:10.5px;line-height:13.3px;text-align:justify;color:#777}
.about p + p{clear:both;padding-top:7px}

.quote{left:673px;top:690px;width:225px;height:248px;background:var(--orange);box-shadow:0 8px 10px -6px rgba(0,0,0,.35)}
.quote h2{background:var(--dark);color:var(--white);font-size:15px;font-weight:700;height:39px;line-height:39px;padding-left:12px;letter-spacing:.3px}
.field{position:absolute;left:10px;width:206px;background:var(--white);border:1px solid #f3d29a;font-size:11.5px;color:#999;padding:6px 7px;letter-spacing:.4px}
.send{position:absolute;right:9px;top:214px;background:var(--orange-deep);color:var(--white);font-size:12.5px;padding:6px 9px;filter:brightness(.97)}

.footer-col h4{font-size:12.5px;font-weight:400;color:#222;margin-bottom:17px}
.footer-col ul{list-style:none}
.footer-col li{font-size:10.5px;color:#777;height:20px;letter-spacing:.3px}
.contact-row{display:flex;gap:8px;font-size:10px;color:#777;line-height:12px;letter-spacing:.5px;margin-bottom:13px}
.newsletter p{font-size:10.5px;line-height:12px;color:#777;letter-spacing:.3px;width:184px}
.news-form{display:flex;margin-top:12px;width:184px;height:27px}
.news-form span{flex:1;border:1px solid #ddd;font-size:11.5px;color:#555;padding:6px 7px}
.news-form b{background:var(--orange);color:var(--white);font-weight:400;font-size:11.5px;padding:7px 6px}

.copyright{left:100px;top:1160px;font-size:10.5px;color:#777;letter-spacing:.3px}
.social{right:100px;top:1154px;display:flex;gap:11px}
.social span{width:20px;height:20px;background:#c4c4c4}
</style>
</head>
<body>

<header>
  <div class="abs brand"><span class="brand-mark"></span>Harbourline Press Works</div>
  <div class="abs phone">
    <span class="phone-icon"><svg width="12" height="12" viewBox="0 0 24 24"><path fill="#fff" d="M6.6 10.8a15 15 0 0 0 6.6 6.6l2.2-2.2c.3-.3.7-.4 1-.2 1.1.4 2.3.6 3.6.6.6 0 1 .4 1 1V20c0 .6-.4 1-1 1A17 17 0 0 1 3 4c0-.6.4-1 1-1h3.5c.6 0 1 .4 1 1 0 1.3.2 2.5.6 3.6.1.3 0 .7-.2 1z"/></svg></span>
    416-555-0147
  </div>
  <nav class="abs main-nav">
    <a class="active" href="#">Home</a><a href="#">About Us</a><a href="#">Our Services</a><a href="#">News</a><a href="#">Contact Us</a>
  </nav>
</header>

<section class="abs slider">
  <div class="slide">
    <div class="slide-photo" role="img" aria-label="Photo of a smiling businesswoman in a bright office with colleagues blurred behind"></div>
    <div class="slide-title">Digital Printing</div>
    <div class="slide-tag">Smart Solutions for your Business</div>
    <ul class="slide-points">
      <li><span class="tick"><svg width="14" height="14" viewBox="0 0 14 14"><path d="M2 7.5l3 3 7-7" stroke="#fff" stroke-width="2.4" fill="none"/></svg></span>Lorem ipsum dolor sit amet.</li>
      <li><span class="tick"><svg width="14" height="14" viewBox="0 0 14 14"><path d="M2 7.5l3 3 7-7" stroke="#fff" stroke-width="2.4" fill="none"/></svg></span>Nulla at quam arcu, eu dapibus ipsum.</li>
      <li><span class="tick"><svg width="14" height="14" viewBox="0 0 14 14"><path d="M2 7.5l3 3 7-7" stroke="#fff" stroke-width="2.4" fill="none"/></svg></span>Sed ac tellus at urna dignissim congue.</li>
    </ul>
    <span class="arrow prev"><svg width="12" height="14" viewBox="0 0 12 14"><path d="M8 2L3 7l5 5" stroke="#fff" stroke-width="2.2" fill="none"/></svg></span>
    <span class="arrow next"><svg width="12" height="14" viewBox="0 0 12 14"><path d="M4 2l5 5-5 5" stroke="#fff" stroke-width="2.2" fill="none"/></svg></span>
  </div>
</section>
<div class="abs slider-shadow"></div>

<section class="abs services">
  <div class="service">
    <svg viewBox="0 0 84 44" width="84" style="margin-top:10px;height:44px"><g fill="none" stroke="var(--red)" stroke-width="3"><rect x="2" y="4" width="28" height="36" rx="2"/><rect x="54" y="4" width="28" height="36" rx="2"/></g><g stroke="var(--red)" stroke-width="3"><path d="M8 13h16M8 19h16M8 25h16M8 31h16M60 13h16M60 19h16M60 25h16M60 31h16"/></g><path d="M34 15h6v-6l11 13-11 13v-6h-6z" fill="var(--red)"/></svg>
    <h3>Legal Copy</h3>
    <p>Lorem ipsum dolor sit amet, con-sectetur adipiscing elit. Nunc eget magna enim.</p>
  </div>
  <div class="service">
    <svg viewBox="0 0 60 60" width="60"><rect x="14" y="2" width="32" height="18" rx="2" fill="var(--red)"/><rect x="2" y="20" width="56" height="28" rx="5" fill="var(--red)"/><rect x="14" y="38" width="32" height="20" fill="#fff" stroke="var(--red)" stroke-width="3"/><path d="M19 45h22M19 51h22" stroke="var(--red)" stroke-width="2.5"/><circle cx="50" cy="28" r="2.5" fill="#fff"/></svg>
    <h3>Digital Printing</h3>
    <p>Lorem ipsum dolor sit amet, con-sectetur adipiscing elit. Nunc eget magna enim.</p>
  </div>
  <div class="service">
    <svg viewBox="0 0 60 60" width="60"><path d="M14 8h38a8 8 0 0 1 0 16H46v28a8 8 0 0 1-8 8H10a8 8 0 0 1 0-16h4z" fill="var(--red)"/><circle cx="52" cy="16" r="4" fill="#fff"/><circle cx="10" cy="52" r="4" fill="#fff"/><path d="M20 22h18M20 30h18M20 38h14" stroke="#fff" stroke-width="2.5"/></svg>
    <h3>Offset Printing</h3>
    <p>Lorem ipsum dolor sit amet, con-sectetur adipiscing elit. Nunc eget magna enim.</p>
  </div>
  <div class="service">
    <svg viewBox="0 0 68 60" width="68"><path d="M2 24L34 2l32 22v32H2z" fill="var(--red)"/><rect x="14" y="12" width="40" height="28" fill="#fff"/><path d="M24 20h20M24 26h20M24 32h20" stroke="var(--red)" stroke-width="2.5"/><path d="M2 24l32 22 32-22v34H2z" fill="var(--red)" stroke="#fff" stroke-width="1.5"/><path d="M2 58l24-18M66 58L42 40" stroke="#fff" stroke-width="1.5"/></svg>
    <h3>Mailing</h3>
    <p>Lorem ipsum dolor sit amet, con-sectetur adipiscing elit. Nunc eget magna enim.</p>
  </div>
</section>

<div class="abs divider" style="left:80px;top:666px;width:838px"></div>

<section class="abs about">
  <h2>Who We Are</h2>
  <div class="about-photo" role="img" aria-label="Photo of a cheerful office team with a smiling woman in front"></div>
  <p>Lorem ipsum dolor sit amet, consectetur adipiscing elit. Nunc eget magna enim. Morbi at tortor enim, quis gravida lacus. Phasellus tempor lorem nec ipsum adipiscing mattis. Integer placerat dictum eros, vitae pulvinar neque vestibulum et. Proin imperdiet, felis vel consectetur ornare, dui leo pulvinar erat, eu dictum justo nibh vel quam. Mauris interdum vehicula enim, eu aliquet tortor volutpat sit amet. Fusce nec augue metus.</p>
  <p>Morbi dui nisi, luctus ut faucibus ut, pellentesque nec metus. Curabitur consectetur, eros ac convallis elementum, neque nunc molestie leo, eu accumsan erat nisi sit amet quam. Quisque ac eros odio. Aliquam hendrerit pulvinar elit, at blandit tortor tincidunt non. Praesent ultricies enim est, in blandit sem. Nam tincidunt ipsum et eros tempus a sodales tortor sagittis. Ut ut dolor mauris. Quisque sed magna neque. Maecenas vel condimentum dolor.</p>
</section>

<aside class="abs quote">
  <h2>Get a Free Quote</h2>
  <div class="field" style="top:55px">Name</div>
  <div class="field" style="top:93px">Email</div>
  <div class="field" style="top:132px;height:74px">Write a message</div>
  <div class="send">Send Message</div>
</aside>

<div class="abs divider" style="left:80px;top:971px;width:838px"></div>

<footer>
  <div class="abs footer-col" style="left:100px;top:999px">
    <h4>Navigation</h4>
    <ul><li>Home</li><li>About Us</li><li>Our Services</li><li>News</li><li>Contact Us</li></ul>
  </div>
  <div class="abs footer-col" style="left:289px;top:999px">
    <h4>Our Services</h4>
    <ul><li>Suspendisse</li><li>Nullam fermentum</li><li>Integer ornare</li><li>Proin iaculis</li><li>Praesent ac</li></ul>
  </div>
  <div class="abs footer-col" style="left:478px;top:999px">
    <h4>Contact us</h4>
    <div class="contact-row"><svg width="10" height="12" viewBox="0 0 10 12"><path d="M5 0a4 4 0 0 0-4 4c0 3 4 8 4 8s4-5 4-8a4 4 0 0 0-4-4z" fill="#999"/><circle cx="5" cy="4" r="1.5" fill="#fff"/></svg><span>480 Harbour ST East Concourse<br>Level Toronto, On M5V 2K8</span></div>
    <div class="contact-row"><svg width="10" height="10" viewBox="0 0 24 24"><path fill="#999" d="M6.6 10.8a15 15 0 0 0 6.6 6.6l2.2-2.2c.3-.3.7-.4 1-.2 1.1.4 2.3.6 3.6.6.6 0 1 .4 1 1V20c0 .6-.4 1-1 1A17 17 0 0 1 3 4c0-.6.4-1 1-1h3.5c.6 0 1 .4 1 1 0 1.3.2 2.5.6 3.6.1.3 0 .7-.2 1z"/></svg><span>416-555-0147</span></div>
    <div class="contact-row"><svg width="10" height="10" viewBox="0 0 10 8"><rect width="10" height="8" fill="#999"/><path d="M0 0l5 4 5-4" stroke="#fff" fill="none"/></svg><span>dana@hpwgroup-example.ca</span></div>
  </div>
  <div class="abs footer-col newsletter" style="left:715px;top:999px">
    <h4>Newsletter</h4>
    <p>Lorem ipsum dolor sit amet, consectetur adipiscing elit. Nunc eget magna enim.</p>
    <div class="news-form"><span>Email Address</span><b>Submit</b></div>
  </div>

  <div class="abs divider" style="left:100px;top:1147px;width:798px;background:var(--line)"></div>
  <div class="abs copyright">Copyright © 2013 HPW. All Right Reserved.</div>
  <div class="abs social"><span></span><span></span><span></span></div>
  <div class="abs divider" style="left:100px;top:1184px;width:798px;background:var(--line)"></div>
</footer>

</body>
</html>
```